Rural photograpy business card design

I need a business card for my photography business, marisol dovey photography. I would like my logo and pre designed font used on the card. Also my business specialises in photographing rural australia (e.g. shearing sheds, livestock, landscapes, farms), so a rural or country feel to the card would be great. I would like to keep the colours fresh but not too overpowering or juvenile.

Hi,

Could you please add my facebook page to the card - www.snapfolk.net/Marisol/Dovey/Photography.
Thanks,
Marisol.

Reason: I have uploaded two photos I would like either one used on the card.

Target Market(s)

Farmers, country people from their mid twenties onwards

Industry/Entity Type

Business

Contact Information for Business Card

Marisol Dovey Photography. Marisol Pendergast. 1295 Wirrabilla-Kontee Road, Kontee Qld 4871. 0471620394.

Requirements
Must have
• My pre-designed logo and font. Also please add my facebook address - www.snapfolk.net/MarisolDovey/Photography.
Please use one of the photos I have provided.
Should not have
• Peoples faces on the card.

```html
<!DOCTYPE html>
<html lang="en">
<head>
<meta charset="utf-8">
<title>Marisol Dovey Photography – Business Card</title>
<link href="https://fonts.googleapis.com/css2?family=Mulish:wght@400;500;700&display=swap" rel="stylesheet">
<style>
  :root {
    --canvas: #ece4d8;
    --card-blue: #5a73a8;
    --card-blue-deep: #4d669b;
    --gold: #c49a5a;
    --white: #ffffff;
    --ink: #1e1e22;
    --badge-light: #dfe4ef;
    --sky-top: #5f78b4;
    --sky-low: #8a96a8;
    --land: #3a2c20;
  }
  * { margin: 0; padding: 0; box-sizing: border-box; }
  html, body { width: 1200px; height: 1000px; overflow: hidden; }
  body {
    background: var(--canvas);
    font-family: "Mulish", sans-serif;
    position: relative;
  }
  .card {
    position: absolute;
    overflow: hidden;
    box-shadow: 0 8px 22px rgba(0,0,0,0.28);
  }
  /* Front */
  .card--front {
    left: 160px; top: 50px; width: 780px; height: 450px;
    background: var(--card-blue);
    color: var(--white);
  }
  .front__scenery {
    position: absolute; inset: 0;
    background: linear-gradient(180deg, var(--card-blue) 0%, var(--card-blue-deep) 100%);
  }
  .identity { position: absolute; left: 58px; top: 132px; }
  .identity__name { font-weight: 700; font-size: 29px; letter-spacing: 1px; }
  .identity__role { font-weight: 400; font-size: 23px; letter-spacing: 12px; margin-top: 2px; }
  .badge {
    position: absolute; border-radius: 50%;
    display: flex; align-items: center; justify-content: center; text-align: center;
  }
  .badge--front {
    width: 250px; height: 250px; right: 8px; top: -20px;
    background: var(--gold); color: var(--white);
  }
  .badge__name {
    font-weight: 500; font-size: 24px; line-height: 1.3; letter-spacing: 1px;
    padding-top: 10px;
  }
  .contact {
    position: absolute; list-style: none;
    font-weight: 700; font-size: 15px; letter-spacing: 1px; line-height: 1.4;
  }
  .contact li { display: flex; align-items: flex-start; gap: 16px; margin-bottom: 24px; }
  .contact__icon { flex: 0 0 auto; width: 22px; height: 22px; }
  .contact--left { left: 72px; top: 345px; }
  .contact--right { left: 552px; top: 302px; }
  .contact__square { width: 20px; height: 20px; background: var(--gold); margin-top: 2px; }
  /* Back */
  .card--back {
    left: 240px; top: 525px; width: 810px; height: 410px;
  }
  .back__photo {
    position: absolute; inset: 0;
    background: linear-gradient(180deg, var(--sky-top) 0%, var(--sky-low) 50%, var(--land) 100%);
  }
  .badge--back {
    width: 250px; height: 250px; right: 0; top: -10px;
    background: var(--badge-light); color: var(--ink);
  }
</style>
</head>
<body>
  <section class="card card--front">
    <div class="front__scenery" role="img" aria-label="Faint blue-toned rural landscape of gum trees across the card"></div>

    <div class="identity">
      <h1 class="identity__name">Marisol Pendergast</h1>
      <p class="identity__role">Photographer</p>
    </div>

    <div class="badge badge--front">
      <p class="badge__name">MARISOL DOVEY<br>PHOTOGRAPHY</p>
    </div>

    <ul class="contact contact--left">
      <li>
        <svg class="contact__icon" viewBox="0 0 24 24" aria-hidden="true">
          <path fill="#c49a5a" d="M6.6 2.5l3 .6 1.2 4.6-2.2 1.6c.9 2.4 2.7 4.4 5 5.6l1.7-2.1 4.6 1.3.6 3c.1.7-.4 1.4-1.1 1.5C10.6 19.6 4.3 13.3 5.1 4c.1-.8.8-1.6 1.5-1.5z"/>
        </svg>
        <span>+6047-162-0394</span>
      </li>
      <li>
        <span class="contact__square" aria-hidden="true"></span>
        <span>snapfolk.net/Marisol/<br>Dovey/Photography</span>
      </li>
    </ul>

    <ul class="contact contact--right">
      <li>
        <svg class="contact__icon" viewBox="0 0 24 24" aria-hidden="true">
          <path fill="#c49a5a" d="M12 1.5a7 7 0 0 0-7 7c0 5.3 7 14 7 14s7-8.7 7-14a7 7 0 0 0-7-7zm0 9.7a2.8 2.8 0 1 1 0-5.6 2.8 2.8 0 0 1 0 5.6z"/>
        </svg>
        <span>1295 Wirrabilla-<br>Kontee Road,<br>Kontee Qld,<br>4871</span>
      </li>
    </ul>
  </section>

  <section class="card card--back">
    <div class="back__photo" role="img" aria-label="Photograph of gum trees silhouetted against a blue sky at sunrise over open farmland"></div>
    <div class="badge badge--back">
      <p class="badge__name">MARISOL DOVEY<br>PHOTOGRAPHY</p>
    </div>
  </section>
</body>
</html>
```